Flyer Mail out

Need something urgently designed.

I need a flyer done double sided I have provided CWDG photos and the writing. I do not have any dental surgery stock photos as such but this can be used. We are a mobile dental company that goes out to schools and provide free dental services.

I have attached the written document and would like it double sided A4 paper.

The colours I want is Aqua, Light Blue, dark blue, grey and white.

Just need it designed beautifully and professionally to go out to principals to contact us and use our services.

If you would like more info have a look at our Chatterloop page Coastline Wandering Dental Group

```html
<!DOCTYPE html>
<html lang="en">
<head>
<meta charset="utf-8">
<title>CWDG School Flyer</title>
<link rel="stylesheet" href="https://fonts.googleapis.com/css2?family=Montserrat:wght@800;900&family=Open+Sans:wght@400;600;700&display=swap">
<style>
  :root {
    --page-bg: #3a3a3c;
    --paper: #ffffff;
    --sand: #e9e3da;
    --sand-light: #f5f2ed;
    --brand-blue: #1a5fb4;
    --band-blue: #1565c0;
    --ink: #2f3338;
    --aqua: #8fd3e6;
    --sky: #4d8fd6;
    --navy: #253a8a;
    --grey: #8c8f94;
  }
  * { box-sizing: border-box; margin: 0; padding: 0; }
  html, body { width: 1200px; height: 993px; overflow: hidden; }
  body {
    background: var(--page-bg);
    font-family: "Open Sans", Arial, sans-serif;
    color: var(--ink);
    position: relative;
  }
  .flyer {
    position: absolute;
    left: 280px; top: 44px;
    width: 640px; height: 905px;
    background: linear-gradient(180deg, var(--sand-light) 0%, var(--sand) 100%);
    overflow: hidden;
  }
  .hero-photo {
    position: absolute; left: 230px; top: 0;
    width: 410px; height: 330px;
    background: linear-gradient(135deg, #f3d9c4 0%, #e8b99c 45%, #9fd6e6 100%);
  }
  .hero-fade {
    position: absolute; left: 200px; top: 0; width: 120px; height: 330px;
    background: linear-gradient(90deg, var(--sand-light) 0%, rgba(245,242,237,0) 100%);
  }
  .site-url {
    position: absolute; right: 18px; top: 12px;
    font-size: 10px; font-weight: 700; color: var(--ink);
  }
  .intro { position: absolute; left: 36px; top: 34px; width: 220px; }
  .headline {
    font-family: "Montserrat", Arial, sans-serif; font-weight: 900;
    color: var(--brand-blue); font-size: 30px; line-height: 1.02;
    text-transform: uppercase; margin-bottom: 18px;
  }
  .stat { font-size: 12.5px; line-height: 1.45; }
  .source { font-size: 11px; font-weight: 700; margin-top: 12px; line-height: 1.4; }
  .bridge {
    position: absolute; left: 40px; top: 344px; width: 560px;
    text-align: center; font-size: 12.5px; line-height: 1.45;
  }
  .cta-band {
    position: absolute; left: 0; top: 404px; width: 640px; height: 62px;
    background: var(--band-blue); color: #fff;
    display: flex; flex-direction: column; justify-content: center; align-items: center;
    font-family: "Open Sans", Arial, sans-serif; font-weight: 700;
    font-size: 19px; line-height: 1.2; text-align: center;
  }
  .team-card {
    position: absolute; left: 40px; top: 490px; width: 290px; height: 228px;
    background: var(--paper); padding: 12px;
    box-shadow: 0 6px 14px rgba(0,0,0,0.25);
  }
  .team-photo {
    width: 100%; height: 140px;
    background: linear-gradient(180deg, #dfe5ea 0%, #9aa7b3 60%, #5a6470 100%);
  }
  .brand { display: flex; align-items: center; gap: 8px; margin-top: 14px; }
  .brand-mark { width: 22px; height: 22px; background: var(--ink); flex: none; }
  .brand-name { font-size: 12px; font-weight: 700; color: var(--ink); line-height: 1.2; }
  .brand-tagline { font-size: 8px; letter-spacing: 0.08em; color: var(--grey); margin-left: 30px; margin-top: 3px; }
  .contact {
    position: absolute; left: 352px; top: 488px; width: 260px;
    font-size: 12.5px; line-height: 1.5;
  }
  .contact p + p { margin-top: 6px; }
  .contact strong { font-weight: 700; }
  .gallery {
    position: absolute; left: 0; top: 740px; width: 640px; height: 165px;
    display: grid; grid-template-columns: 1fr 1fr 1fr 1fr; gap: 4px;
  }
  .tile-truck { background: linear-gradient(180deg, #3f86d8 0%, #9cc6ef 55%, #6d8a4a 100%); }
  .tile-staff { background: linear-gradient(180deg, #4a8fdc 0%, #2a3f96 70%, #1d2c6e 100%); }
  .tile-care { background: linear-gradient(135deg, #eef1f3 0%, #c9d3da 60%, #8aa3b4 100%); }
  .tile-team { background: linear-gradient(135deg, #f2efe9 0%, #d9c7a8 50%, #2f3338 100%); }
</style>
</head>
<body>
  <article class="flyer">
    <div class="hero-photo" role="img" aria-label="Smiling young girl in a dental chair holding a dental mirror"></div>
    <div class="hero-fade"></div>
    <span class="site-url">www.cwdg.net.au</span>

    <section class="intro">
      <h1 class="headline">Our focus is on education &amp; prevention</h1>
      <p class="stat">1 in 5 children between the ages of 4-8 years of age will suffer from tooth decay or dental caries as a result of poor dental hygiene</p>
      <p class="source">(ref; The Southern College of Child Health)</p>
    </section>

    <p class="bridge">Thus, leading to possible dental destruction to their adult teeth. This, in conjunction with diet, lifestyle and social welfare can be contribution to the increase of child absenteeism.</p>

    <div class="cta-band">
      <span>Book us now for 2015 and help us,</span>
      <span>bring back your student’s “bright smile”</span>
    </div>

    <figure class="team-card">
      <div class="team-photo" role="img" aria-label="Dental team standing in front of the mobile dental truck"></div>
      <div class="brand">
        <span class="brand-mark"></span>
        <span class="brand-name">Coastline Wandering Dental Group</span>
      </div>
      <p class="brand-tagline">INNOVATION WITH A SMILE</p>
    </figure>

    <section class="contact">
      <p>To find out about our procedures or to book your school for 2015 and take advantage of this opportunity. Please visit our website <strong>www.cwdg.net.au</strong> or email me at <strong>mara.l@cwdg.net.au</strong></p>
      <p>Or to speak to one of our friendly staff, call us directly on <strong>(02) 5550 1842</strong></p>
      <p>In addition, feel free to visit <strong>Chatterloop/Chirpwire/Workmesh</strong> to see regular updates, features, special offers and daily tips regarding our services.</p>
    </section>

    <div class="gallery">
      <div class="tile-care" role="img" aria-label="Dentist treating a patient in the mobile surgery"></div>
      <div class="tile-team" role="img" aria-label="Two dental staff members smiling"></div>
      <div class="tile-staff" role="img" aria-label="Staff in blue uniforms outdoors"></div>
      <div class="tile-truck" role="img" aria-label="Mobile dental truck parked under blue sky"></div>
    </div>
  </article>
</body>
</html>
```